We want to create a postcard that welcomes our customers to the neighborhood. We want the front of the postcard to say "Welcome to the neighborhood" and have our store info:
Vinehaven 27 Wine & Spirits
412 8th Ave (29th Street)
(646) 555-0178
www.vinehaven27shop.example
Free neighborhood deliveries

On the back of the postcard we want to let our customers know of our Daily Specials.
Daily Specials 10% off at Vinehaven 27
Magnum Mondays : All 1.5L Wines
Tuscan Tuesdays : All 750ml Italian Wines
Wine-in-a-Box Wednesdays : All boxed Wines
Thirsty Thursdays : All 750ml Sparkling/Champagne
French Fridays : All 750ml French Wines
Surfin' Saturdays : All 750ml Californian Wines
South American & Spanish Sundays : All 750ml
We are thinking of black and white for both sides but we are open to any ideas and suggestions on color and wording!Thanks

Requirements
Must have
• Store info
Nice to have
• A Clean layout
• Nice and simple
Should not have
• Overcrowded wording

```html
<!DOCTYPE html>
<html lang="en">
<head>
<meta charset="utf-8">
<title>Vinehaven 27 Wine &amp; Spirits – Welcome Postcard</title>
<link href="https://fonts.googleapis.com/css2?family=Oswald:wght@200;300;400;500&family=Great+Vibes&display=swap" rel="stylesheet">
<style>
  :root{
    --backdrop:#ececec;
    --ink:#2a2829;
    --band:#3b393a;
    --white:#ffffff;
    --red:#d32431;
    --red-dark:#9e1620;
    --grey-light:#bdbdbd;
    --grey-mid:#7d7d7d;
  }
  *{margin:0;padding:0;box-sizing:border-box}
  html,body{width:907px;height:1200px;overflow:hidden;background:var(--backdrop)}
  body{position:relative;font-family:'Oswald',sans-serif;color:var(--white)}

  .postcard{position:absolute;left:115px;width:681px;height:529px;overflow:hidden;background:var(--ink);box-shadow:0 2px 8px rgba(0,0,0,.25)}
  .postcard--front{top:55px}
  .postcard--back{top:628px}

  .photo{position:absolute;inset:0}
  .photo--storefront{background:linear-gradient(180deg,#5a5a5a 0%,#8c8c8c 35%,#c9c9c9 55%,#6d6d6d 80%,#9a9a9a 100%)}
  .photo--pour{background:radial-gradient(ellipse at 30% 55%,#2b2b2b 0%,#5c5c5c 35%,#9a9a9a 65%,#b5b5b5 100%)}

  .bands{position:absolute;inset:0;width:100%;height:100%}

  .glass-inset{position:absolute;left:233px;top:220px;width:190px;height:190px;border-radius:50%;
    background:radial-gradient(circle at 50% 60%,#5a2a2a 0%,#8a7070 30%,#bbb 60%,#777 100%);
    border:6px solid #e4e4e4;box-shadow:0 0 0 3px #8a8a8a}

  .badge{position:absolute;border-radius:50%;display:flex;flex-direction:column;align-items:center;justify-content:center;text-align:center;
    background:radial-gradient(circle at 40% 35%,var(--red) 0%,var(--red) 55%,var(--red-dark) 100%);color:var(--white);text-transform:uppercase;border:2px solid #f1f1f1}
  .badge--delivery{left:230px;top:401px;width:104px;height:104px}
  .badge--delivery .badge__big{font-size:28px;font-weight:500;line-height:1}
  .badge--delivery .badge__small{font-size:12px;font-weight:400;line-height:1.1;margin-top:3px}
  .badge--specials{left:318px;top:289px;width:146px;height:146px}
  .badge--specials .badge__small{font-size:18px;font-weight:500;line-height:1;white-space:nowrap;letter-spacing:.2px}
  .badge--specials .badge__offer{display:flex;align-items:center;margin-top:4px;white-space:nowrap}
  .badge--specials .badge__big{font-size:50px;font-weight:500;line-height:1}
  .badge--specials .badge__turned{display:inline-block;font-size:22px;font-weight:500;line-height:1;transform:rotate(90deg);width:24px;margin-left:2px}

  .store-name{position:absolute;font-family:'Oswald',sans-serif;font-weight:300;color:var(--white);line-height:1}
  .store-name__main{display:block;font-size:27px}
  .store-name__sub{display:block;font-size:11px;letter-spacing:1px;margin-top:3px;text-align:center}
  .postcard--front .store-name{left:33px;top:398px}
  .postcard--back .store-name{left:488px;top:434px}

  .store-info{position:absolute;left:35px;top:457px;list-style:none;font-size:11.5px;font-weight:300;font-family:'Oswald',sans-serif;letter-spacing:.3px}
  .store-info li{display:flex;align-items:center;gap:7px;height:19px}
  .store-info svg{width:9px;height:9px;fill:var(--white)}

  .welcome{position:absolute;right:26px;top:372px;width:300px;text-align:right;font-weight:normal}
  .welcome__lead{display:block;font-family:'Oswald',sans-serif;font-weight:200;font-size:40px;line-height:1;padding-right:13px;transform:scaleX(.82);transform-origin:right center}
  .welcome__title{display:block;font-family:'Great Vibes',cursive;font-size:58px;line-height:1;margin-top:6px}

  .specials{position:absolute;left:285px;top:36px;width:366px;list-style:none}
  .specials li{display:flex;align-items:baseline;height:34px;font-size:16.5px;letter-spacing:-.1px}
  .specials__day{font-weight:500;white-space:nowrap}
  .specials__dots{flex:1;border-bottom:2px dotted var(--white);margin:0 2px;transform:translateY(-4px);min-width:6px}
  .specials__offer{font-weight:300;white-space:nowrap}
</style>
</head>
<body>

<section class="postcard postcard--front" aria-label="Postcard front">
  <div class="photo photo--storefront" role="img" aria-label="Black and white photo of the wine shop storefront with window displays and passers-by"></div>
  <svg class="bands" viewBox="0 0 681 529" preserveAspectRatio="none" aria-hidden="true">
    <polygon points="0,360 681,245 681,265 0,380" fill="#d9d9d9"/>
    <polygon points="0,372 681,258 681,529 0,529" fill="var(--ink)"/>
  </svg>
  <div class="glass-inset" role="img" aria-label="Close-up photo of red wine poured into a glass"></div>
  <div class="badge badge--delivery">
    <span class="badge__big">Free</span>
    <span class="badge__small">Neighborhood<br>Deliveries</span>
  </div>
  <div class="store-name">
    <span class="store-name__main">Vinehaven 27</span>
    <span class="store-name__sub">wine &amp; spirits</span>
  </div>
  <ul class="store-info">
    <li><svg viewBox="0 0 10 10"><path d="M5 0a3.5 3.5 0 0 0-3.5 3.5C1.5 6 5 10 5 10s3.5-4 3.5-6.5A3.5 3.5 0 0 0 5 0zm0 5a1.5 1.5 0 1 1 0-3 1.5 1.5 0 0 1 0 3z"/></svg>412 8th Ave (29th Street)</li>
    <li><svg viewBox="0 0 10 10"><path d="M0 1h10v8H0z M2.5 2.5 3.8 2l1 1.8-.8.6c.4.9 1 1.5 1.9 1.9l.6-.8 1.8 1-.5 1.3C4.9 7.6 2.4 5.1 2.5 2.5z" fill-rule="evenodd"/></svg>(646) 555-0178</li>
    <li><svg viewBox="0 0 10 10"><path d="M0 2h10v6H0z M.8 2.6 5 5.6l4.2-3" fill-rule="evenodd"/></svg>www.vinehaven27shop.example</li>
  </ul>
  <h1 class="welcome">
    <span class="welcome__lead">Welcome to the</span>
    <span class="welcome__title">Neighborhood</span>
  </h1>
</section>

<section class="postcard postcard--back" aria-label="Postcard back">
  <div class="photo photo--pour" role="img" aria-label="Black and white photo of wine pouring from a bottle into a glass"></div>
  <svg class="bands" viewBox="0 0 681 529" preserveAspectRatio="none" aria-hidden="true">
    <polygon points="0,455 681,360 681,402 0,470" fill="#b8b8b8"/>
    <polygon points="0,463 681,396 681,404 0,472" fill="#f2f2f2"/>
    <polygon points="0,471 681,403 681,529 0,529" fill="var(--ink)"/>
  </svg>
  <ul class="specials">
    <li><span class="specials__day">Magnum Mondays</span><span class="specials__dots"></span><span class="specials__offer">All 1.5L Wines</span></li>
    <li><span class="specials__day">Tuscan Tuesdays</span><span class="specials__dots"></span><span class="specials__offer">All 750ml Italian Wines</span></li>
    <li><span class="specials__day">Wine-in-a-Box Wednesdays</span><span class="specials__dots"></span><span class="specials__offer">All boxed Wines</span></li>
    <li><span class="specials__day">Thirsty Thursdays</span><span class="specials__dots"></span><span class="specials__offer">All 750ml Sparkling/Champagne</span></li>
    <li><span class="specials__day">French Fridays</span><span class="specials__dots"></span><span class="specials__offer">All 750ml French Wines</span></li>
    <li><span class="specials__day">Surfin' Saturdays</span><span class="specials__dots"></span><span class="specials__offer">All 750ml Californian Wines</span></li>
    <li><span class="specials__day">South American &amp; Spanish Sundays</span><span class="specials__dots"></span><span class="specials__offer">All 750ml</span></li>
  </ul>
  <div class="badge badge--specials">
    <span class="badge__small">Daily Specials</span>
    <span class="badge__offer"><span class="badge__big">10%</span><span class="badge__turned">Off</span></span>
  </div>
  <div class="store-name">
    <span class="store-name__main">Vinehaven 27</span>
    <span class="store-name__sub">wine &amp; spirits</span>
  </div>
</section>

</body>
</html>
```